Commercial facility maintenance

I need a card design that helps my salesmen make contact with new clients, our product is facility maintenance and heavy industrial maintenance

```html
<!DOCTYPE html>
<html lang="en">
<head>
<meta charset="utf-8">
<title>Harlow Millworks LLC – Business Card</title>
<link href="https://fonts.googleapis.com/css2?family=Montserrat:wght@400;500;700;800&display=swap" rel="stylesheet">
<style>
  :root{
    --bg:#d9d9da;
    --paper:#ffffff;
    --ink:#000000;
    --charcoal:#3b3e43;
    --brand-red:#9e2129;
    --line-red:#d3202d;
    --light:#ffffff;
  }
  *{box-sizing:border-box;margin:0;padding:0}
  html,body{width:1200px;height:896px;overflow:hidden;background:var(--bg)}
  body{position:relative;font-family:'Montserrat',sans-serif}

  .card{
    position:absolute;left:334px;width:528px;height:300px;
    border-radius:24px;overflow:hidden;background:var(--paper);
    box-shadow:0 14px 22px rgba(0,0,0,.18);
  }
  .card--front{top:126px}
  .card--back{top:475px}

  .card__art{position:absolute;inset:0;width:100%;height:100%}

  .brand{
    position:absolute;right:22px;top:42px;
    display:flex;align-items:center;gap:12px;
  }
  .brand__dot{width:40px;height:40px;border-radius:50%;background:var(--brand-red)}
  .brand__name{
    font-weight:800;font-size:25px;line-height:1.05;color:var(--charcoal);
    letter-spacing:.5px;
  }

  .person{position:absolute;left:23px;top:148px;color:var(--light)}
  .person__name{font-weight:800;font-size:25px;color:var(--brand-red);letter-spacing:.3px;line-height:1}
  .person__role{font-weight:400;font-size:14px;margin-top:8px;letter-spacing:.4px}

  .divider{position:absolute;left:23px;right:16px;top:207px;height:2px;background:var(--line-red)}

  .contacts{position:absolute;left:23px;top:222px;list-style:none;color:var(--light);font-size:14px}
  .contacts li{display:flex;align-items:center;gap:7px;height:21px}
  .contacts svg{width:11px;height:11px;fill:var(--line-red)}

  .address{
    position:absolute;right:16px;top:243px;text-align:right;
    color:var(--light);font-size:14px;line-height:21px;
  }

  .emblem{
    position:absolute;inset:0;display:flex;align-items:center;justify-content:center;gap:14px;
  }
  .emblem__dot{width:54px;height:54px;border-radius:50%;background:var(--brand-red)}
  .emblem__name{font-weight:800;font-size:30px;line-height:1.05;color:var(--charcoal);letter-spacing:.5px}
</style>
</head>
<body>

  <section class="card card--front">
    <svg class="card__art" viewBox="0 0 528 300" preserveAspectRatio="none" aria-hidden="true">
      <path d="M10,125 C140,97 230,132 313,155 C410,180 480,150 528,124" fill="none" stroke="var(--brand-red)" stroke-width="8"/>
      <path d="M0,135 C140,105 230,140 313,163 C410,188 480,160 528,138 L528,300 L0,300 Z" fill="var(--ink)"/>
    </svg>

    <div class="brand">
      <span class="brand__dot"></span>
      <span class="brand__name">HARLOW<br>MILLWORKS LLC</span>
    </div>

    <div class="person">
      <p class="person__name">DANA RELLER</p>
      <p class="person__role">OWNER</p>
    </div>

    <div class="divider"></div>

    <ul class="contacts">
      <li><svg viewBox="0 0 12 12"><path d="M1 4c0-2 2-3 5-3s5 1 5 3v1H8V4H4v1H1zM3 6h6l2 5H1z"/></svg>555-014-2298</li>
      <li><svg viewBox="0 0 12 12"><path d="M0 2h12v8H0zM1 3l5 4 5-4"/></svg>dreller@mailbox.com</li>
      <li><svg viewBox="0 0 12 12"><circle cx="6" cy="6" r="5.5"/></svg>harlowmillworksllc.com</li>
    </ul>

    <p class="address">Your address, City<br>State, Zip 10000</p>
  </section>

  <section class="card card--back">
    <div class="emblem">
      <span class="emblem__dot"></span>
      <span class="emblem__name">HARLOW<br>MILLWORKS LLC</span>
    </div>
  </section>

</body>
</html>
```